Fitness Supplements Packaging Project (Renders of Existing Products)

Dorvane Athletic Works (DAW) produces sports supplements that help with training performance and recovery. Our products are designed to help you get lean, fit and enjoying exercise in all its forms.

DAW requires product renders for our current product line-up of 9 products with 15 total variants. We require individual product renders and also 4 product line-ups. Examples will be provided below along with detailed imagery of our existing labels and packaging (renders MUST use identical DAW packaging and labels)

Single Shot Renders (one product per render):

Found in the 'PROTEIN SERIES' file pack:

DAW Summit Whey (Choc, Strawberry, Vanilla) Size: 235 x 335mm
DAW Velocity Whey (Choc, Strawberry, Vanilla) Size: 235 x 335mm
DAW Trim Balance Whey (Choc, Strawberry, Vanilla) Size: 190 x 265mm

Found in the 'TRAINING TOOLS' file pack:

DAW Steadier, Size: 160 x 230mm
DAW Igniter, Size: 160 x 230mm
DAW Amplifier, Size: 160 x 230mm

Found in the 'BASICS SERIES' file pack:
DAW Creatine, Size: 190 x 265mm
DAW L- Glutamine, Size: 190 x 265mm
DAW BCAA, Size: 190 x 265mm

Series Shots:

“DAW PROTEIN SERIES”

One shot that contains the three whey products, DAW Velocity, DAW Summit, DAW Trim Balance in that order from left to right. Only one flavour variant is required (chocolate)

“DAW TRAINING TOOLS”

One shot that contains the DAW Amplifier, DAW Igniter, DAW Steadier in that order from left to right.

“DAW BASICS”

One shot that contains the DAW Creatine, DAW L-Glutamine, and DAW BCAA in any order

FULL PRODUCT SHOTS

One shot with all products. Only one flavour variant is required for the whey products.

Detailed images of the existing packaging will be provided.

All currently existing labels will be provided in both .jpeg and .pdf formats. If other formats are required, please contact us.

Examples from competitors (THESE EXAMPLES USE PLASTIC TUBS - OUR PRODUCTS USE FOIL PACKAGING, PLEASE SEE THE PHOTOS OF OUR PRODUCTS PROVIDED IN THE FILES BELOW):

Single product render: http://www.brenvalshop.example/Images/Products/1000/Harlow-Fuel/Harlow-Fuel-Prime-Blend-100-Whey-Double-Rich-Chocolate-512038467190.jpg

Product Line-up: http://www.gymrolla.example/wp-content/uploads/2012/06/HF_Fuel.jpg

NOTE: Renders must be done using our existing packaging and NOT in tubs as seen in the examples above.

Attached File Descriptions:
Attached are all the files you should require to complete this project.

File 1: Basics Series Pack - This pack contains all required files to create Basics series renders including labels for all product variants and examples.

File 2: Logos set - All our current logos if you should need them.

File 3: Foil Packaging Pack - High quality images of our current foil packaging bags.

File 4: Training Tools pack - This pack contains all required files to create Training Tool renders including labels for all product variants and examples.

File 5: Protein Series Pack. This pack contains all required files to create protein series renders including labels for all product variants and examples.

If further files are required, please get in touch and we shall provide them ASAP.

Thanks and good luck!

Target Market(s)

Fitness and athletes. M/F; 18-30 yo; Engaging, bold, fun, strong, attitude.

Industry/Entity Type

Fitness

Requirements
Must have
• *All designs must be provided in editable file formats such as an illustrator .ai file or an Adobe Photoshop .psd file.

*All renders must use our existing packaging and labels which will be provided in the "Files" section.

*All render previews must have no background (.png format). A shadow/reflection can be added in for effect if you wish as seen in above examples.

*As Stated in the description above, there MUST be individual product renders for each product and flavour variant (9 products and 15 total variants). There MUST also be lineup renders of the "Protein Series", "Training Tools Series", "Basics Series".
Should not have
• -Renders with packages which are different from our current black foil bags.

-Try not to make the renders overly shiny - they need to be done in way that enables them to be used in any type of advertising material.

```html
<!DOCTYPE html>
<html lang="en">
<head>
<meta charset="utf-8">
<title>DAW Training Tools – Labels</title>
<link href="https://fonts.googleapis.com/css2?family=Russo+One&family=Arimo:wght@400;700&display=swap" rel="stylesheet">
<style>
  :root {
    --page: #ffffff;
    --label-bg: #141414;
    --label-edge: #262626;
    --text: #d9d9d9;
    --muted: #9a9a9a;
    --green: #4cc35a;
    --pink: #e0358f;
    --blue: #29aee6;
    --red: #e8242c;
    --orange: #e0532b;
  }
  * { box-sizing: border-box; margin: 0; padding: 0; }
  html, body { width: 1200px; height: 832px; overflow: hidden; background: var(--page); }
  body { font-family: "Arimo", Arial, sans-serif; color: var(--text); }

  .lineup {
    display: flex; justify-content: center; align-items: center;
    gap: 36px; width: 1200px; height: 832px;
  }

  .label {
    position: relative; width: 360px; height: 520px;
    background: var(--label-bg); border-radius: 12px;
    border: 1px solid var(--label-edge);
    padding: 30px 26px 22px;
  }
  .label--amplifier { --accent: var(--green); --flavour: var(--pink); }
  .label--igniter { --accent: var(--blue); --flavour: var(--green); }
  .label--steadier { --accent: var(--red); --flavour: var(--orange); }

  .edge { position: absolute; font-size: 6.5px; color: var(--accent); white-space: nowrap; }
  .edge--top { top: 12px; left: 26px; right: 26px; overflow: hidden; }
  .edge--left { left: 12px; top: 200px; transform: rotate(-90deg); transform-origin: left top; }
  .edge--right { right: 4px; top: 30px; transform: rotate(90deg); transform-origin: left top; left: 352px; }

  .brand { text-align: center; margin-top: 10px; }
  .brand__mark { display: inline-flex; align-items: center; gap: 6px; }
  .brand__dot { width: 18px; height: 18px; border-radius: 50%; background: var(--accent); }
  .brand__name { font-family: "Russo One", sans-serif; font-size: 30px; color: var(--accent); line-height: 1; }
  .brand__tagline { font-size: 5.5px; letter-spacing: 1.5px; color: var(--muted); margin-top: 3px; }

  .product { margin-top: 18px; text-align: center; }
  .product__name { font-family: "Russo One", sans-serif; font-size: 30px; color: var(--accent); letter-spacing: 1px; line-height: 1; }
  .product__flavour { font-size: 13px; color: var(--flavour); margin-top: 4px; letter-spacing: .3px; }

  .panel { display: grid; grid-template-columns: 148px 1fr; gap: 8px; margin-top: 16px; font-size: 7.5px; line-height: 1.35; }
  .panel__col { display: flex; flex-direction: column; gap: 6px; }
  .box { border: 1px solid var(--accent); border-radius: 3px; padding: 5px 6px; }
  .box--storage { background: var(--accent); color: #f4f4f4; text-align: center; border: none; }
  .box__title { color: var(--accent); text-transform: uppercase; }
  .box p + p { margin-top: 8px; }

  .facts { border: 1px solid var(--accent); border-radius: 3px; align-self: start; }
  .facts__row { display: grid; grid-template-columns: 1fr 38px 22px; padding: 3px 5px; border-bottom: 1px solid var(--accent); gap: 2px; }
  .facts__row:last-child { border-bottom: none; }
  .facts__row span:nth-child(2) { color: var(--accent); }
  .facts__row span:nth-child(3) { color: var(--accent); text-align: right; }
  .facts__row--plain { border-bottom: none; }

  .footnote { position: absolute; right: 26px; bottom: 18px; font-size: 7px; color: var(--accent); }
</style>
</head>
<body>
<main class="lineup">

  <article class="label label--amplifier">
    <p class="edge edge--top">use by those with serious medical conditions or pregnant or lactating women. Consult your physician</p>
    <p class="edge edge--left">Warning: This product is not intended for</p>
    <p class="edge edge--right">before use. Keep out of reach of children</p>
    <header class="brand">
      <div class="brand__mark"><span class="brand__dot"></span><span class="brand__name">DAW</span></div>
      <p class="brand__tagline">DORVANE · ATHLETIC · WORKS</p>
    </header>
    <div class="product">
      <h2 class="product__name">AMPLIFIER</h2>
      <p class="product__flavour">RASPBERRY FLAVOUR</p>
    </div>
    <section class="panel">
      <div class="panel__col">
        <div class="box box--storage">Storage: Keep dry in cool, dark place<br>400g NET</div>
        <div class="box">
          <p class="box__title">Directions</p>
          <p style="margin-top:0">Add 1 scoop of DAW Amplifier to 200ml of water. DAW Amplifier is best consumed before intense exercise.</p>
          <p class="box__title" style="margin-top:4px">Ingredients</p>
          <p style="margin-top:0">DAW Amplifier Blend (L-Citruline DL-Malate, AAKG, Beta-Alanine, Taurine, Caffine) Flavour, Sucralose, Colour.</p>
        </div>
        <div class="box">
          <p>This product is not intended to diagnose, treat, cure or prevent any disease.</p>
          <p>This product is manufactured in New Zealand with local and imported ingredients.</p>
          <p>Manufactured in a facility that also processes peanuts, wheat and eggs</p>
        </div>
      </div>
      <div class="facts">
        <div class="facts__row"><span>Serving Size</span><span>10g</span><span></span></div>
        <div class="facts__row"><span>Servings per container</span><span>40</span><span></span></div>
        <div class="facts__row"><span>Amount Per Serving</span><span>Daily Value %*</span><span></span></div>
        <div class="facts__row"><span>Calories</span><span>8</span><span></span></div>
        <div class="facts__row"><span>DAW Amplifier Blend</span><span>9.43g</span><span>**%</span></div>
        <div class="facts__row facts__row--plain"><span>Contains:</span><span></span><span></span></div>
        <div class="facts__row facts__row--plain"><span>L-Citruline DL-Malate</span><span></span><span></span></div>
        <div class="facts__row facts__row--plain"><span>AAKG</span><span></span><span></span></div>
        <div class="facts__row facts__row--plain"><span>Beta-Alanine</span><span></span><span></span></div>
        <div class="facts__row facts__row--plain"><span>Taurine</span><span></span><span></span></div>
        <div class="facts__row"><span>Caffeine</span><span></span><span></span></div>
      </div>
    </section>
    <p class="footnote">Product contains Caffeine</p>
  </article>

  <article class="label label--igniter">
    <p class="edge edge--top">use by those with serious medical conditions or pregnant or lactating women. Consult your physician</p>
    <p class="edge edge--left">Warning: This product is not intended for</p>
    <p class="edge edge--right">before use. Keep out of reach of children</p>
    <header class="brand">
      <div class="brand__mark"><span class="brand__dot"></span><span class="brand__name">DAW</span></div>
      <p class="brand__tagline">DORVANE · ATHLETIC · WORKS</p>
    </header>
    <div class="product">
      <h2 class="product__name">IGNITER</h2>
      <p class="product__flavour">LIME FLAVOUR</p>
    </div>
    <section class="panel">
      <div class="panel__col">
        <div class="box box--storage">Storage: Keep dry in cool, dark place<br>400g NET</div>
        <div class="box">
          <p class="box__title">Directions</p>
          <p style="margin-top:0">Add 1 scoop of DAW Igniter to 200ml of water. Shake and enjoy! DAW Igniter is best consumed during intense exercise.</p>
          <p class="box__title" style="margin-top:4px">Ingredients</p>
          <p style="margin-top:0">DAW BCAA Blend (L-Leucine, L-Isoleucine, L-Valine), Emulsifier (320), Flavour, Sucralose, Citric acid, Colour</p>
        </div>
        <div class="box">
          <p>This product is not intended to diagnose, treat, cure or prevent any disease.</p>
          <p>This product is manufactured in New Zealand with local and imported ingredients.</p>
          <p>Allergen Information: Contains soy ingredients.</p>
          <p>Manufactured in a facility that also processes peanuts, wheat and eggs</p>
        </div>
      </div>
      <div class="facts">
        <div class="facts__row"><span>Serving Size</span><span>8g</span><span></span></div>
        <div class="facts__row"><span>Servings per container</span><span>50</span><span></span></div>
        <div class="facts__row"><span>Amount Per Serving</span><span>Daily Value %*</span><span></span></div>
        <div class="facts__row"><span>Calories</span><span>26</span><span></span></div>
        <div class="facts__row"><span>L-Leucine</span><span>2500mg</span><span>**%</span></div>
        <div class="facts__row"><span>L-Isoleucine</span><span>1250mg</span><span>**%</span></div>
        <div class="facts__row"><span>L-Valine</span><span>1250mg</span><span>**%</span></div>
      </div>
    </section>
  </article>

  <article class="label label--steadier">
    <p class="edge edge--top">use by those with serious medical conditions or pregnant or lactating women. Consult your physician</p>
    <p class="edge edge--left">Warning: This product is not intended for</p>
    <p class="edge edge--right">before use. Keep out of reach of children</p>
    <header class="brand">
      <div class="brand__mark"><span class="brand__dot"></span><span class="brand__name">DAW</span></div>
      <p class="brand__tagline">DORVANE · ATHLETIC · WORKS</p>
    </header>
    <div class="product">
      <h2 class="product__name">STEADIER</h2>
      <p class="product__flavour">ORANGE FLAVOUR</p>
    </div>
    <section class="panel">
      <div class="panel__col">
        <div class="box box--storage">Storage: Keep dry in cool, dark place<br>400g NET</div>
        <div class="box">
          <p class="box__title">Directions</p>
          <p style="margin-top:0">Add 1 scoop of DAW Steadier to 250ml of water. DAW Steadier is best consumed after intense exercise.</p>
          <p class="box__title" style="margin-top:4px">Ingredients</p>
          <p style="margin-top:0">Creatine, L-Glutamine, Dextrose, Maltodextrin, Sucrose, Flavour, Sucralose, Citric Acid, Colour.</p>
        </div>
        <div class="box">
          <p>This product is not intended to diagnose, treat, cure or prevent any disease.</p>
          <p>This product is manufactured in New Zealand with local and imported ingredients.</p>
          <p>Manufactured in a facility that also processes peanuts, wheat and eggs</p>
        </div>
      </div>
      <div class="facts">
        <div class="facts__row"><span>Serving Size</span><span>10g</span><span></span></div>
        <div class="facts__row"><span>Servings per container</span><span>40</span><span></span></div>
        <div class="facts__row"><span>Amount Per Serving</span><span>Daily Value %*</span><span></span></div>
        <div class="facts__row"><span>Calories</span><span>17</span><span></span></div>
        <div class="facts__row"><span>DAW Steadier Blend</span><span>8.67g</span><span>**%</span></div>
        <div class="facts__row"><span>Contains:</span><span></span><span></span></div>
        <div class="facts__row"><span>Creatine</span><span>5g</span><span>**%</span></div>
        <div class="facts__row"><span>L-Glutamine</span><span>1g</span><span>**%</span></div>
        <div class="facts__row"><span>Carbohydrate</span><span>2.67g</span><span></span></div>
        <div class="facts__row"><span>Sugar</span><span>2.67g</span><span></span></div>
      </div>
    </section>
    <p class="footnote">Product may contain phenylalanine</p>
  </article>

</main>
</body>
</html>
```